Flyer for the Radiant Harvest Worship Day 2020

I am looking to create a flyer for a one day prayer retreat our church is organizing.
This flyer will be posted on social media, websites and will also be printed so it can be mailed to people.
I am looking for something professional, with good use of our logo and band colors (logo colors).
I am counting on the designer's skill, creativity, art and knowledge of media communication to produce a flyer that will effectively and quickly convey the message we are trying to spread.
CONTENT OF THE FLYER:
Event title: Radiant Harvest Worship Day
Date: Tuesday July 2nd, 2020
Time: 11:00AM - 7:00PM
Belmora Hotel, 4876 Willowmere Street, Portland, Maine 04987 (Room: Evergrove)
Event Key words to highlight what the event is about: Prayer, Sharing the Word, Panel discussion, prophecy, Impartation.
Key phrases:
A one day prayer retreat.
Jesus Chris is Lord
Contact info:
www.toluvek.org
Phone: 207 555 0183
Email: contact@brightmeadowfold.org

```html
<!DOCTYPE html>
<html lang="en">
<head>
<meta charset="utf-8">
<title>Radiant Harvest Worship Day 2020</title>
<link href="https://fonts.googleapis.com/css2?family=Open+Sans:wght@400;600;700;800&display=swap" rel="stylesheet">
<style>
  :root {
    --ink: #14151b;
    --orange: #e8923a;
    --white: #ffffff;
    --soft: #d9d9dc;
    --rule: #3a3b42;
    --photo-dark: #1b1714;
    --photo-mid: #4a3a2e;
    --photo-warm: #8a6a52;
  }
  * { margin: 0; padding: 0; box-sizing: border-box; }
  html, body { width: 797px; height: 1200px; overflow: hidden; background: var(--ink); }
  body { font-family: "Open Sans", Arial, sans-serif; color: var(--white); }
  .flyer { position: relative; width: 797px; height: 1200px; background: var(--ink); overflow: hidden; }
  .flyer > * { z-index: 1; }

  .brand { position: absolute; top: 80px; left: 0; width: 100%; display: flex; justify-content: center; align-items: center; gap: 14px; }
  .brand-dot { width: 22px; height: 22px; border-radius: 50%; background: var(--orange); }
  .brand-name { font-size: 60px; font-weight: 400; letter-spacing: 4px; color: var(--white); line-height: 1; }

  .title { position: absolute; top: 262px; left: 0; width: 100%; text-align: center; font-weight: 800; line-height: 1.08; }
  .title-top { display: block; font-size: 53px; color: var(--orange); letter-spacing: 0.5px; }
  .title-bottom { display: block; font-size: 53px; color: var(--white); }

  .tagline-band { position: absolute; top: 398px; left: 101px; width: 631px; height: 52px; background: var(--orange); display: flex; align-items: center; justify-content: center; font-size: 28px; font-weight: 400; color: var(--white); white-space: nowrap; }
  .tagline-band .divider { margin: 0 18px 0 8px; }

  .event-when { position: absolute; top: 482px; left: 102px; }
  .day { font-size: 28px; font-weight: 700; color: var(--orange); margin-left: 72px; line-height: 1.2; }
  .date { font-size: 29px; font-weight: 700; color: var(--white); line-height: 1.25; }
  .when-rule { width: 268px; height: 1px; background: var(--rule); margin: 14px 0 10px; }
  .time { font-size: 30px; font-weight: 700; color: var(--white); }
  .time .dash { color: var(--orange); }

  .venue { position: absolute; top: 648px; left: 102px; font-size: 15.5px; font-weight: 600; line-height: 1.5; color: var(--white); white-space: nowrap; }
  .venue .venue-name { color: var(--orange); }

  .highlights { position: absolute; top: 497px; left: 524px; list-style: none; }
  .highlights li { display: flex; align-items: center; gap: 20px; font-size: 20px; font-weight: 400; color: var(--soft); height: 35px; }
  .tick { width: 17px; height: 17px; flex: none; }

  .flyer > .photo { position: absolute; top: 700px; left: 0; width: 797px; height: 427px; z-index: 0;
    background:
      radial-gradient(ellipse at 30% 65%, var(--photo-warm) 0%, transparent 45%),
      radial-gradient(ellipse at 72% 55%, var(--photo-warm) 0%, transparent 42%),
      linear-gradient(180deg, var(--ink) 0%, var(--photo-dark) 20%, var(--photo-mid) 60%, var(--photo-dark) 100%); }

  .contact-bar { position: absolute; bottom: 0; left: 0; width: 100%; height: 73px; background: var(--ink); display: flex; align-items: center; justify-content: center; gap: 14px; font-size: 19.5px; font-weight: 700; color: var(--white); white-space: nowrap; }
  .contact-item { display: flex; align-items: center; gap: 8px; }
  .contact-icon { width: 17px; height: 17px; flex: none; }
  .sep { width: 2px; height: 24px; background: var(--white); }
</style>
</head>
<body>
<main class="flyer">
  <div class="photo" role="img" aria-label="Photo of several people's clasped hands resting on a wooden table in prayer"></div>

  <header class="brand">
    <span class="brand-dot"></span>
    <span class="brand-name">TOLUVEK</span>
  </header>

  <h1 class="title">
    <span class="title-top">RADIANT HARVEST</span>
    <span class="title-bottom">WORSHIP DAY</span>
  </h1>

  <p class="tagline-band">A one day prayer retreat<span class="divider">|</span>Jesus Chris is Lord</p>

  <section class="event-when">
    <p class="day">TUESDAY</p>
    <p class="date">JULY&nbsp; 2ND 2020</p>
    <div class="when-rule"></div>
    <p class="time">11:00AM <span class="dash">-</span> 7:00PM</p>
  </section>

  <p class="venue"><span class="venue-name">Belmora Hotel,</span> 4876 Willowmere Street,<br>Portland, Maine 04987 (Room: Evergrove)</p>

  <ul class="highlights">
    <li><svg class="tick" viewBox="0 0 20 20"><circle cx="10" cy="10" r="10" fill="#e8923a"/><path d="M5.5 10.3l3 3 6-6.3" fill="none" stroke="#14151b" stroke-width="2"/></svg>Prayer</li>
    <li><svg class="tick" viewBox="0 0 20 20"><circle cx="10" cy="10" r="10" fill="#e8923a"/><path d="M5.5 10.3l3 3 6-6.3" fill="none" stroke="#14151b" stroke-width="2"/></svg>Sharing The Word</li>
    <li><svg class="tick" viewBox="0 0 20 20"><circle cx="10" cy="10" r="10" fill="#e8923a"/><path d="M5.5 10.3l3 3 6-6.3" fill="none" stroke="#14151b" stroke-width="2"/></svg>Panel Discussion</li>
    <li><svg class="tick" viewBox="0 0 20 20"><circle cx="10" cy="10" r="10" fill="#e8923a"/><path d="M5.5 10.3l3 3 6-6.3" fill="none" stroke="#14151b" stroke-width="2"/></svg>Prophecy</li>
    <li><svg class="tick" viewBox="0 0 20 20"><circle cx="10" cy="10" r="10" fill="#e8923a"/><path d="M5.5 10.3l3 3 6-6.3" fill="none" stroke="#14151b" stroke-width="2"/></svg>Impartation</li>
  </ul>

  <footer class="contact-bar">
    <span class="contact-item">
      <svg class="contact-icon" viewBox="0 0 20 16"><rect x="1" y="2" width="18" height="12" fill="#e8923a"/><path d="M1 2l9 7 9-7" fill="none" stroke="#14151b" stroke-width="1.6"/></svg>
      contact@brightmeadowfold.org
    </span>
    <span class="sep"></span>
    <span class="contact-item">
      <svg class="contact-icon" viewBox="0 0 20 20"><path d="M5 2l3 4-2 2c1 2.5 3.5 5 6 6l2-2 4 3-2 3C9 18 2 11 2 4z" fill="#e8923a"/></svg>
      207 555 0183
    </span>
    <span class="sep"></span>
    <span class="contact-item">
      <svg class="contact-icon" viewBox="0 0 20 20"><circle cx="10" cy="10" r="8.5" fill="none" stroke="#e8923a" stroke-width="1.8"/><ellipse cx="10" cy="10" rx="3.5" ry="8.5" fill="none" stroke="#e8923a" stroke-width="1.4"/><path d="M1.5 10h17M3 5.5h14M3 14.5h14" stroke="#e8923a" stroke-width="1.4"/></svg>
      www.toluvek.org
    </span>
  </footer>
</main>
</body>
</html>
```